New Business Card Design Project VORALDI-Italy

we are VORALDI-Italy
our company in the market for 3 years we are luxury cosmetic company and its about time for a facelift :)
i will like to have elegant luxurious and unique business card
that will give the person that get it a unique, luxurious and elegant impression
I'm VERY OPEN FOR NEW IDEAS , even duo i add a few files of things that i see on line and i like them

i add my logo as well
my website is VORALDI.COM
(if you would like to see the main style that we have)

Target Market(s)

adult that have money :)

Industry/Entity Type

Business

Contact Information for Business Card

Name - Paul Voraldi
Position - CEO and CO Founder
address - 4718 E Danbury
telephone - 555-318-4402
email - paul@voraldi-example.com
fax - 555-318-4402
website - VORALDI.COM

Colors
000000
959595
fbee3e
ffffff

Requirements
Must have
• big logo in GOLD color
• elegant look
• impressive
Nice to have
• not must but maybe classy pattern background
• not must but maybe emblem
• maybe clear plastic business card
Should not have
• colors
• images

```html
<!DOCTYPE html>
<html lang="en">
<head>
<meta charset="utf-8">
<title>VORALDI Italy – Business Card</title>
<link rel="stylesheet" href="https://fonts.googleapis.com/css2?family=Tinos:wght@400;700&family=PT+Sans:wght@400&display=swap">
<style>
  :root {
    --backdrop: #4a4a4a;
    --card-black: #111111;
    --card-tone: #262626;
    --gold: #d9b23a;
    --gold-light: #f0d061;
    --white: #ffffff;
    --grey: #959595;
  }
  * { margin: 0; padding: 0; box-sizing: border-box; }
  html, body { width: 1200px; height: 900px; overflow: hidden; }
  body { background: var(--backdrop); position: relative; }

  .card {
    position: absolute;
    top: 184px;
    width: 303px;
    height: 492px;
    border-radius: 12px;
    overflow: hidden;
  }
  .card--front { left: 319px; }
  .card--back  { left: 646px; width: 305px; }

  .card__pattern {
    position: absolute; inset: 0;
    background:
      radial-gradient(ellipse at 50% 30%, rgba(60,60,60,0.55), rgba(0,0,0,0) 60%),
      linear-gradient(160deg, var(--card-tone) 0%, var(--card-black) 45%, #1a1a1a 70%, var(--card-black) 100%);
  }

  .centered { position: absolute; left: 0; width: 100%; text-align: center; }

  .seal {
    position: absolute;
    border-radius: 50%;
    border: 3px solid var(--gold);
    display: flex; align-items: center; justify-content: center;
  }
  .card--front .seal { left: 73px; top: 62px; width: 156px; height: 156px; }
  .card--back  .seal { left: 99px; top: 141px; width: 106px; height: 106px; }
  .seal__name {
    font-family: "Tinos", serif;
    font-size: 22px;
    color: var(--gold);
    letter-spacing: 1px;
  }

  .person__name {
    top: 269px;
    font-family: "Tinos", serif;
    font-weight: 700;
    font-size: 19px;
    color: var(--gold);
    letter-spacing: 0.3px;
  }
  .person__title {
    top: 295px;
    font-family: "PT Sans", sans-serif;
    font-size: 13px;
    color: var(--white);
  }
  .divider {
    position: absolute;
    left: 101px; width: 100px; height: 1px;
    background: var(--gold);
  }
  .divider--top { top: 325px; }
  .divider--bottom { top: 432px; }

  .contact-icons {
    position: absolute; top: 341px; left: 120px;
    display: flex; gap: 6px;
  }
  .contact-icons svg { width: 15px; height: 15px; display: block; }

  .contact {
    top: 366px;
    font-family: "PT Sans", sans-serif;
    font-size: 13px;
    line-height: 18px;
    color: var(--white);
  }
  .address {
    top: 445px;
    font-family: "PT Sans", sans-serif;
    font-size: 13px;
    color: var(--white);
  }

  .brand__name {
    top: 268px;
    font-family: "Tinos", serif;
    font-size: 48px;
    line-height: 50px;
    color: var(--gold);
    letter-spacing: 1px;
  }
  .brand__rule {
    position: absolute;
    left: 34px; top: 324px;
    width: 236px; height: 3px;
    background: var(--gold);
    border-radius: 2px;
  }
  .brand__country {
    top: 334px;
    font-family: "Tinos", serif;
    font-size: 17px;
    color: var(--gold);
  }
  .brand__web {
    top: 435px;
    font-family: "Tinos", serif;
    font-weight: 700;
    font-size: 16px;
    color: var(--gold);
  }
</style>
</head>
<body>

<section class="card card--front">
  <div class="card__pattern" role="img" aria-label="Faint repeating tone-on-tone emblem pattern on black"></div>
  <div class="seal"><span class="seal__name">VORALDI</span></div>

  <p class="centered person__name">PAUL VORALDI</p>
  <p class="centered person__title">CEO and CO Founder</p>
  <div class="divider divider--top"></div>

  <div class="contact-icons">
    <svg viewBox="0 0 16 16" aria-label="Phone"><circle cx="8" cy="8" r="8" fill="#d9b23a"/><path d="M5 4.5c.6-.4 1.2 0 1.5.6l.4.9c.1.4 0 .7-.3.9l-.4.3c.4.9 1.1 1.6 2 2l.3-.4c.2-.3.5-.4.9-.3l.9.4c.6.3 1 .9.6 1.5-.5.8-1.3 1-2.2.6-1.8-.8-3.2-2.2-4-4-.4-.9-.2-1.700.3-2.500z" fill="#141414"/></svg>
    <svg viewBox="0 0 16 16" aria-label="Fax"><circle cx="8" cy="8" r="8" fill="#d9b23a"/><rect x="5.5" y="4" width="5" height="3" fill="#141414"/><rect x="4" y="7" width="8" height="4.5" rx="0.6" fill="#141414"/><rect x="6" y="9.5" width="4" height="1" fill="#d9b23a"/></svg>
    <svg viewBox="0 0 16 16" aria-label="Email"><circle cx="8" cy="8" r="8" fill="#d9b23a"/><rect x="4" y="5.2" width="8" height="5.6" rx="0.6" fill="#141414"/><path d="M4.3 5.6 8 8.4l3.7-2.8" stroke="#d9b23a" stroke-width="0.8" fill="none"/></svg>
  </div>

  <p class="centered contact">555-318-4402<br>555-318-4402<br>paul@voraldi-example.com</p>
  <div class="divider divider--bottom"></div>
  <p class="centered address">4718 E Danbury</p>
</section>

<section class="card card--back">
  <div class="card__pattern" role="img" aria-label="Faint repeating tone-on-tone emblem pattern on black"></div>
  <div class="seal"></div>
  <p class="centered brand__name">VORALDI</p>
  <div class="brand__rule"></div>
  <p class="centered brand__country">ITALY</p>
  <p class="centered brand__web">VORALDI.COM</p>
</section>

</body>
</html>
```